I am a surgeon that operates on gynaecological cancer. Wish a design and logo for letter head.

Design should include my name: Dr. Kiran Mudaly, qualifications: FTELSWOB, CGO. and state that I am a Gynaecological Oncologist and Advanced Laparoscopic Surgeon.
As for a logo. As all cancer is related to DNA, I think that that double helix could be used to symbolise a female shape, exaggerating the abdomen to suggest a mass.

Reason: Extended to view changes I have asked for.

```html
<!DOCTYPE html>
<html lang="en">
<head>
<meta charset="utf-8">
<title>Dr. Kiran Mudaly — Letterhead</title>
<link rel="stylesheet" href="https://fonts.googleapis.com/css2?family=Tinos:wght@400;700&display=swap">
<style>
  :root {
    --band-strong: #bcd99a;
    --band-soft: #e4f0d4;
    --ink-green: #2f6b2a;
    --mark-green: #5f9a3e;
    --mark-fill: #d8eac2;
    --watermark-grey: #e9ebe8;
    --footer-band: #cfe3b4;
    --paper: #ffffff;
  }
  html, body {
    margin: 0;
    padding: 0;
    width: 893px;
    height: 1200px;
    overflow: hidden;
    background: var(--paper);
  }
  .letterhead {
    position: relative;
    width: 893px;
    height: 1200px;
    background: var(--paper);
    font-family: "Tinos", "Times New Roman", serif;
    color: var(--ink-green);
  }
  .header-band {
    position: absolute;
    top: 0; left: 0;
    width: 100%;
    height: 140px;
    background: linear-gradient(90deg, var(--band-strong) 0%, #cde4b0 55%, var(--band-soft) 100%);
  }
  .brand-mark {
    position: absolute;
    left: 40px;
    top: 20px;
    width: 74px;
    height: 74px;
  }
  .practitioner-name {
    position: absolute;
    left: 126px;
    top: 20px;
    margin: 0;
    font-size: 44px;
    font-weight: 400;
    line-height: 1;
    white-space: nowrap;
  }
  .qualifications {
    font-size: 15px;
    letter-spacing: 0.5px;
    margin-left: 14px;
    vertical-align: 4px;
  }
  .speciality {
    position: absolute;
    left: 126px;
    top: 89px;
    margin: 0;
    font-size: 22.5px;
    line-height: 1;
    white-space: nowrap;
  }
  .page-watermark {
    position: absolute;
    left: 22px;
    top: 800px;
    width: 170px;
    height: 170px;
  }
  .footer-band {
    position: absolute;
    left: 0; bottom: 0;
    width: 100%;
    height: 72px;
    background: var(--footer-band);
    display: flex;
    flex-direction: column;
    align-items: center;
    justify-content: center;
    gap: 3px;
    font-size: 11.5px;
    color: var(--ink-green);
  }
  .footer-band p { margin: 0; }
</style>
</head>
<body>
  <main class="letterhead">
    <header class="header-band">
      <svg class="brand-mark" viewBox="0 0 74 74" aria-hidden="true">
        <circle cx="37" cy="37" r="34" fill="var(--mark-fill)" stroke="var(--mark-green)" stroke-width="4"/>
      </svg>
      <h1 class="practitioner-name">Dr. Kiran Mudaly<span class="qualifications">FTELSWOB, CGO</span></h1>
      <p class="speciality">Gynaecological Oncologist and Advanced Laparoscopic Surgeon.</p>
    </header>

    <svg class="page-watermark" viewBox="0 0 170 170" aria-hidden="true">
      <circle cx="85" cy="85" r="78" fill="none" stroke="var(--watermark-grey)" stroke-width="14"/>
    </svg>

    <footer class="footer-band">
      <p class="footer-address">14 Harbour Lane, Westridge Medical Centre, Suite 3, Durban North 4051</p>
      <p class="footer-contact">Contact: +27 31 555 0142 Hospital: 031 555 0199</p>
    </footer>
  </main>
</body>
</html>
```